Lumo Voyages
business cards & letterhead
Lumo Voyages -
Creative Brief
Bright & Fun-filled
Corinne Maddox
58214 Birchwood Ln Rockville, MD 20817
lumovoyages@quellnet.example

```html
<!DOCTYPE html>
<html lang="en">
<head>
<meta charset="utf-8">
<title>Lumo Voyages – Business Card</title>
<link href="https://fonts.googleapis.com/css2?family=Open+Sans:wght@400;600;700&display=swap" rel="stylesheet">
<style>
  :root {
    --backdrop: #e9eaec;
    --card: #ffffff;
    --blue-deep: #0a6fb8;
    --blue-light: #2f9be0;
    --green: #8cc63f;
    --green-light: #c4e07a;
    --ink: #4a4f55;
    --rule: #cfd3d7;
    --brand: #1a7fc6;
  }
  * { margin: 0; padding: 0; box-sizing: border-box; }
  html, body {
    width: 1200px; height: 780px; overflow: hidden;
    background: var(--backdrop);
    font-family: "Open Sans", Arial, sans-serif;
  }
  .stage {
    width: 1200px; height: 780px;
    display: flex; align-items: center; justify-content: center;
  }
  .business-card {
    position: relative;
    width: 1000px; height: 572px;
    background: var(--card);
    border-radius: 28px;
    overflow: hidden;
    box-shadow: 0 14px 36px rgba(0,0,0,0.18);
  }
  .card-waves { position: absolute; inset: 0; width: 100%; height: 100%; }
  .holder-name {
    position: absolute; top: 34px; right: 48px;
    color: #fff; font-weight: 700; font-size: 30px;
  }
  .brand {
    position: absolute; left: 56px; bottom: 72px;
    display: flex; align-items: center; gap: 18px;
  }
  .brand-dot {
    width: 74px; height: 74px; border-radius: 50%;
    background: var(--brand);
  }
  .brand-name {
    color: var(--brand); font-weight: 700; font-size: 50px; letter-spacing: 0.5px;
  }
  .contact {
    position: absolute; left: 580px; right: 32px; top: 268px; bottom: 70px;
    border-left: 2px solid var(--rule);
    padding-left: 26px;
    color: var(--ink); font-size: 20px; line-height: 1.4;
    font-style: normal;
    white-space: nowrap;
  }
  .contact-address { margin-bottom: 72px; }
  .contact-line { display: flex; align-items: center; gap: 10px; margin-bottom: 12px; }
  .contact-icon { width: 22px; height: 22px; flex: none; }
</style>
</head>
<body>
<main class="stage">
  <article class="business-card">
    <svg class="card-waves" viewBox="0 0 1000 572" preserveAspectRatio="none" aria-hidden="true">
      <defs>
        <linearGradient id="blueBand" x1="0" y1="0" x2="1" y2="1">
          <stop offset="0" stop-color="var(--blue-light)"/>
          <stop offset="1" stop-color="var(--blue-deep)"/>
        </linearGradient>
        <linearGradient id="greenSwoosh" x1="0" y1="1" x2="1" y2="0">
          <stop offset="0" stop-color="var(--green)"/>
          <stop offset="1" stop-color="var(--green-light)"/>
        </linearGradient>
      </defs>
      <path d="M0,0 H1000 V80 C780,88 540,120 340,200 C210,252 95,300 0,355 Z" fill="url(#blueBand)"/>
      <path d="M0,428 C110,330 320,235 600,190 C390,245 190,330 18,446 Z" fill="url(#greenSwoosh)"/>
    </svg>

    <h1 class="holder-name">Corinne Maddox</h1>

    <div class="brand">
      <span class="brand-dot"></span>
      <span class="brand-name">Lumo Voyages</span>
    </div>

    <address class="contact">
      <p class="contact-address">58214 Birchwood Ln<br>Rockville, MD 20817</p>
      <p class="contact-line">
        <svg class="contact-icon" viewBox="0 0 24 24" aria-hidden="true">
          <path d="M6.6 10.8a15 15 0 0 0 6.6 6.6l2.2-2.2a1 1 0 0 1 1-.25 11.4 11.4 0 0 0 3.6.57 1 1 0 0 1 1 1V20a1 1 0 0 1-1 1A17 17 0 0 1 3 4a1 1 0 0 1 1-1h3.5a1 1 0 0 1 1 1c0 1.25.2 2.45.57 3.57a1 1 0 0 1-.25 1z" fill="var(--brand)"/>
        </svg>
        301-555-0142
      </p>
      <p class="contact-line">
        <svg class="contact-icon" viewBox="0 0 24 24" aria-hidden="true">
          <circle cx="12" cy="12" r="10" fill="none" stroke="var(--brand)" stroke-width="2.4"/>
          <circle cx="12" cy="12" r="3.6" fill="none" stroke="var(--brand)" stroke-width="2.4"/>
          <path d="M15.6 9v4.5a2.4 2.4 0 0 0 4.8 0" fill="none" stroke="var(--brand)" stroke-width="2.4"/>
        </svg>
        lumovoyages@quellnet.example
      </p>
    </address>
  </article>
</main>
</body>
</html>
```